Martial Arts Website

Redevelopment of existing martial arts website.

The academy teaches traditional shaolin martial arts, including Shaolin Kung Fu, Wu Shu, Tai Chi, Qigong and Wing Chun and the site needs to reflect the traditional roots (eg, no tacky boxing imagery)

Existing website is www.copperheron.com.au to get a feel for the desired color scheme (black, green and red). The exact colors can be tweaked though. Please only reuse the logo and font (Karate) - there isnt anything else from the current design that needs to remain.

The current website includes links to a (mark omitted) channel that includes demonstrations of the training conducted to better guide the design.

The new website site map will be:
1. Home
2. Programs - summary page describing each form of training
a. Tiny Otters
b. Kids Kung Fu
c. Youth Kung Fu
d. Adults Kung Fu
e. Wing Chun
f. Tai Chi & Qigong
g. Weaponry Classes
h. 72 Arts of Shaolin Conditioning Program
i. Acrobatics and Wu Shu
j. Fitness Boxing
3. Timetable
4. Coaches - summary page describing all coaches
a. Sifu (Master)
b. Sihing Lou
c. Sihing Kim
d. Sihing Felix
X. ... up to 10 or so coaches
5. Member Zone
6. Contact Us
Updates

Logo now attached to brief - sorry I only have it in PDF

Just to clarify, I am only expecting a PSD design - no HTML required

Reason: Thanks for the designs, we love a lot of them just require a little extra time to tweak the designs and establish the potential. Thanks for your understanding and efforts.

Target Market(s)

Parents, teenagers, young adults, adults, elderly

Industry/Entity Type

Training

Requirements
Must have
• Chinese kung fu dragon imagery throughout the background
Links to Facebook and (mark omitted) channel
Promo/icon in the header "Try 2 free classes now"
Home page should include an embedded (mark omitted) video

```html
<!DOCTYPE html>
<html lang="en">
<head>
<meta charset="utf-8">
<title>Copper Heron Martial Arts Academy – Programs</title>
<link href="https://fonts.googleapis.com/css2?family=Arimo:ital,wght@0,400;0,700;1,700&family=Cinzel:wght@700;900&display=swap" rel="stylesheet">
<style>
:root{
  --black:#000;
  --green:#1f6d1a;
  --green-dark:#14510f;
  --green-text:#1c6a17;
  --red:#b00c0c;
  --white:#fff;
  --ink:#111;
  --grey-top:#8b8b8b;
  --grey-bot:#4a4a4a;
  --nav-text:#444;
}
*{margin:0;padding:0;box-sizing:border-box}
html,body{width:1200px;height:900px;overflow:hidden;background:var(--black);font-family:"Arimo",Arial,sans-serif}
.page{position:relative;width:1200px;height:900px;overflow:hidden}
.backdrop{position:absolute;left:0;top:298px;width:1200px;height:602px;background:radial-gradient(ellipse at 50% 40%,#2a2a2a 0%,#111 60%,#050505 100%)}
.header{position:absolute;left:0;top:0;width:1200px;height:198px;background:var(--black);text-align:center}
.brand{position:absolute;left:0;right:0;top:72px;display:flex;justify-content:center;align-items:center;gap:18px}
.brand-mark{width:34px;height:34px;border-radius:50%;background:var(--green)}
.brand-name{font-family:"Cinzel",serif;font-weight:900;font-size:50px;color:var(--green);letter-spacing:2px}
.tagline{position:absolute;left:0;right:0;top:142px;font-family:"Cinzel",serif;font-weight:700;color:var(--red);font-size:18px;letter-spacing:3px}
.subline{position:absolute;left:0;right:0;top:165px;color:var(--white);font-size:11px;letter-spacing:2px}
.nav{position:absolute;left:0;top:198px;width:1200px;height:40px;background:var(--white)}
.nav ul{list-style:none;position:absolute;left:296px;top:0;display:flex;height:40px;align-items:center}
.nav li{font-size:13px;color:var(--nav-text);padding:0 16px;border-right:1px solid #ccc;line-height:22px}
.nav li:last-child{border:0}
.nav li.active{background:var(--red);color:var(--white);padding:0 10px;margin:0 6px;height:44px;line-height:56px;position:relative;top:-7px;outline:3px solid #e6e6e6}
.band{position:absolute;left:0;top:238px;width:1200px;height:60px;background:linear-gradient(#2a8325,var(--green-dark))}
.band-title{position:absolute;left:306px;top:20px;color:var(--white);font-family:"Cinzel",serif;font-size:22px;font-weight:700}
.band-links{position:absolute;left:480px;top:26px;color:var(--white);font-size:16px;letter-spacing:.5px}
.content{position:absolute;left:178px;top:298px;width:842px;height:602px;background:var(--white)}
.crumbs{position:absolute;left:58px;top:16px;font-size:13px;color:#999}
.program-title{position:absolute;left:56px;top:72px;font-family:"Cinzel",serif;font-weight:900;font-size:22px;color:var(--green-text)}
.program-title small{font-family:"Arimo",sans-serif;font-style:italic;font-weight:400;font-size:14px;margin-left:6px}
.intro{position:absolute;left:58px;top:110px;width:370px;font-size:14px;line-height:18.3px;color:var(--ink)}
.times-btn{position:absolute;left:56px;top:303px;width:248px;height:23px;background:var(--green);color:var(--white);font-size:13px;line-height:23px;padding-left:12px}
.times-btn svg{position:absolute;right:10px;top:4px}
.video{position:absolute;left:461px;top:78px;width:269px;height:248px;background:#000}
.video-title{color:var(--white);font-weight:700;font-size:14px;padding:4px 7px}
.video-frame{position:absolute;left:0;top:26px;width:269px;height:186px;background:linear-gradient(160deg,#4f5f45,#2b3526 60%,#1b1f19)}
.video-bar{position:absolute;left:0;top:212px;width:269px;height:36px;background:linear-gradient(#3a3a3a,#1a1a1a)}
.video-bar .time{position:absolute;left:102px;top:12px;color:#fff;font-size:11px;font-weight:700}
.video-bar .time span{color:#aaa;font-weight:400}
.skills{position:absolute;left:56px;top:358px;width:760px}
.skill h3{font-size:15px;font-style:italic;font-weight:700;color:var(--green-text)}
.skill p{font-size:14px;color:var(--ink);line-height:18px;margin-bottom:18px}
.sidebar{position:absolute;left:966px;top:238px;width:220px;height:450px;background:linear-gradient(var(--grey-top),var(--grey-bot))}
.sidebar h2{font-family:"Cinzel",serif;color:var(--white);font-size:19px;text-align:center;margin:10px 26px 0;padding-bottom:4px;border-bottom:1px dotted #ddd}
.class-list{list-style:none;margin-top:8px}
.class-list li{position:relative;padding-left:54px;height:37.8px;color:var(--white);font-style:italic;font-weight:700;font-size:13px;line-height:14px}
.class-list li small{display:block;font-weight:400;font-size:10px;line-height:12px}
.class-list li svg{position:absolute;left:18px;top:0}
.trial{position:absolute;left:0;bottom:0;width:220px;height:32px;background:var(--green);color:var(--white);font-weight:700;font-size:14px;line-height:32px;padding-left:11px}
.trial svg{position:absolute;right:10px;top:9px}
.dropdown{position:absolute;left:187px;top:238px;width:503px;height:140px;background:rgba(255,255,255,.88);border:1px solid #bbb;box-shadow:0 2px 6px rgba(0,0,0,.35)}
.drop-col{position:absolute;top:9px}
.drop-col h4{font-size:15px;font-style:italic;font-weight:700;color:#222;margin-bottom:5px}
.drop-col li{list-style:none;font-size:13px;color:#222;line-height:23.5px}
</style>
</head>
<body>
<div class="page">
  <div class="backdrop" role="img" aria-label="Faint Chinese calligraphy and dragon imagery on black"></div>

  <header class="header">
    <div class="brand"><span class="brand-mark"></span><span class="brand-name">Copper Heron</span></div>
    <div class="tagline">MARTIAL ARTS ACADEMY</div>
    <div class="subline">TRADITIONAL KUNG FU &amp; TAI CHI TRAINING CENTRE</div>
  </header>

  <nav class="nav">
    <ul>
      <li>HOME</li><li class="active">PROGRAMS</li><li>TIMETABLE</li><li>COACHES</li><li>MEMBER ZONE</li><li>CONTACT US</li>
    </ul>
  </nav>

  <div class="band">
    <div class="band-title">PROGRAMS</div>
    <div class="band-links">Childrens Programs &nbsp;|&nbsp; Adult Programs &nbsp;|&nbsp; Fitness Programs</div>
  </div>

  <main class="content">
    <div class="crumbs">Home &nbsp;&gt;&nbsp; Programs &nbsp;&gt;&nbsp; Childrens Programs</div>
    <h1 class="program-title">Tiny Otters <small>Ages 4 - 6</small></h1>
    <p class="intro">The Copper Heron Tiny Otters program is a detailed curriculum for ages 4 to 6 that focuses on improving a group of very important skills. These skills will help them enter society with a more confident and enthusiastic outlook. They will become better students at school, better listeners at home and more ambitious towards the future. Our program will enhance positive development in a fun and motivating way.</p>
    <div class="times-btn">VIEW CLASS TIMES &amp; DAYS
      <svg width="14" height="16" viewBox="0 0 14 16"><rect x="3" y="0" width="10" height="13" fill="none" stroke="#fff" stroke-width="1.5"/><rect x="0.5" y="3" width="10" height="12.5" fill="#fff"/></svg>
    </div>
    <div class="video">
      <div class="video-title">Tiny Otters Program: Ages 4-6</div>
      <div class="video-frame" role="img" aria-label="Video still of a young class seated on training mats with their instructor"></div>
      <div class="video-bar">
        <svg width="269" height="36" viewBox="0 0 269 36">
          <line x1="8" y1="3" x2="262" y2="3" stroke="#555" stroke-width="3"/>
          <circle cx="9" cy="3" r="6" fill="#ddd"/>
          <polygon points="24,14 24,28 36,21" fill="#aaa"/>
          <polygon points="67,18 71,18 76,13 76,29 71,24 67,24" fill="#aaa"/>
          <circle cx="197" cy="21" r="6" fill="none" stroke="#aaa" stroke-width="2"/>
          <line x1="197" y1="21" x2="197" y2="17" stroke="#aaa" stroke-width="1.5"/>
        </svg>
        <div class="time">0:00 <span>/ 0:00</span></div>
      </div>
    </div>
    <section class="skills">
      <div class="skill"><h3>Focus</h3><p>This skill will develop listening and reaction skills. A better listener means a better student in school.</p></div>
      <div class="skill"><h3>Control</h3><p>Having control means making good decisions. Control builds confidence.</p></div>
      <div class="skill"><h3>Attitude</h3><p>Skills such as respect, honesty, leadership and a positive “can do” attitude are valuable life skills.</p></div>
      <div class="skill"><h3>Balance &amp; Coordination</h3><p>Crucial part of physical development and great for sport and recreational activities.</p></div>
      <div class="skill"><h3>Memory Retention</h3><p>Memory development is good exercise for a child’s brain. A child’s brain need just as much exercise as their</p></div>
    </section>
  </main>

  <aside class="sidebar">
    <h2>ALL CLASSES</h2>
    <ul class="class-list">
      <li><svg width="20" height="20"><circle cx="10" cy="10" r="9" fill="#a00"/><path d="M5 10h7M9 6l4 4-4 4" stroke="#fff" stroke-width="2" fill="none"/></svg>Tiny Otters<small>Ages 4 - 6</small></li>
      <li><svg width="20" height="20"><circle cx="10" cy="10" r="9" fill="#a00"/><path d="M5 10h7M9 6l4 4-4 4" stroke="#fff" stroke-width="2" fill="none"/></svg>Kids Kung Fu<small>Ages 6 - 11</small></li>
      <li><svg width="20" height="20"><circle cx="10" cy="10" r="9" fill="#a00"/><path d="M5 10h7M9 6l4 4-4 4" stroke="#fff" stroke-width="2" fill="none"/></svg>Youth Kung Fu<small>Ages 11 - 15</small></li>
      <li><svg width="20" height="20"><circle cx="10" cy="10" r="9" fill="#a00"/><path d="M5 10h7M9 6l4 4-4 4" stroke="#fff" stroke-width="2" fill="none"/></svg>Adults Kung Fu<small>Ages 15 &amp; over</small></li>
      <li><svg width="20" height="20"><circle cx="10" cy="10" r="9" fill="#a00"/><path d="M5 10h7M9 6l4 4-4 4" stroke="#fff" stroke-width="2" fill="none"/></svg>Wing Chun<small>Ages 13 &amp; over</small></li>
      <li><svg width="20" height="20"><circle cx="10" cy="10" r="9" fill="#a00"/><path d="M5 10h7M9 6l4 4-4 4" stroke="#fff" stroke-width="2" fill="none"/></svg>Tai Chi &amp; Qigong<small>All ages</small></li>
      <li><svg width="20" height="20"><circle cx="10" cy="10" r="9" fill="#a00"/><path d="M5 10h7M9 6l4 4-4 4" stroke="#fff" stroke-width="2" fill="none"/></svg>Weaponry Classes<small>Ages 5 and over</small></li>
      <li><svg width="20" height="20"><circle cx="10" cy="10" r="9" fill="#a00"/><path d="M5 10h7M9 6l4 4-4 4" stroke="#fff" stroke-width="2" fill="none"/></svg>72 Arts of Shaolin<small>Conditioning Program</small></li>
      <li><svg width="20" height="20"><circle cx="10" cy="10" r="9" fill="#a00"/><path d="M5 10h7M9 6l4 4-4 4" stroke="#fff" stroke-width="2" fill="none"/></svg>Acrobatics and Wu Shu<small>Performance Team</small></li>
      <li><svg width="20" height="20"><circle cx="10" cy="10" r="9" fill="#a00"/><path d="M5 10h7M9 6l4 4-4 4" stroke="#fff" stroke-width="2" fill="none"/></svg>Fitness Boxing</li>
    </ul>
    <div class="trial">TRY 2 FREE CLASSES NOW!
      <svg width="10" height="14"><polygon points="0,0 10,7 0,14" fill="#fff"/></svg>
    </div>
  </aside>

  <div class="dropdown">
    <div class="drop-col" style="left:25px"><h4>Childrens Programs</h4><ul><li>Tiny Otters</li><li>Kids Kung Fu</li><li>Youth Kung Fu</li></ul></div>
    <div class="drop-col" style="left:198px"><h4>Adult Programs</h4><ul><li>Adults Kung Fu</li><li>Wing Chun</li><li>Weaponry Classes</li><li>72 Arts of Shaolin</li></ul></div>
    <div class="drop-col" style="left:355px"><h4>Fitness Programs</h4><ul><li>Tai Chi &amp; Qigong</li><li>Acrobatics &amp; Wu Shu</li><li>Fitness Boxing</li></ul></div>
  </div>
</div>
</body>
</html>
```